Kestrane Energy b-card redesign

I would like to redesign the card (and power point template) for kestrane energy. We are a developer/owner/operator of high-tech biomass gasification power plants. We take ag waste like nut shells or fruit pits and convert that into electricity in the 1/2 - 3 MW range. I would like to change our company color from red to golden gate bridge orange (C=0,M=69,,Y=100,B=6).

```html
<!DOCTYPE html>
<html lang="en">
<head>
<meta charset="utf-8">
<title>Kestrane Energy – Business Card</title>
<link rel="stylesheet" href="https://fonts.googleapis.com/css2?family=Questrial&family=Arimo:wght@700&display=swap">
<style>
  :root {
    --bridge-orange: #e8641a;
    --orange-light: #f08a3c;
    --orange-dark: #c9520f;
    --paper: #ffffff;
    --paper-shade: #ececec;
    --ink: #1c1c1c;
    --ink-soft: #444444;
    --muted: #8a8a8a;
    --backdrop: #3b3b3b;
  }
  * { box-sizing: border-box; margin: 0; padding: 0; }
  html, body { width: 1200px; height: 871px; overflow: hidden; }
  body {
    background: var(--backdrop);
    display: flex;
    align-items: center;
    justify-content: center;
    gap: 60px;
  }
  .card {
    position: relative;
    width: 520px;
    height: 297px;
    overflow: hidden;
    box-shadow: 0 10px 30px rgba(0,0,0,.45);
  }
  .wordmark {
    font-family: "Questrial", sans-serif;
    font-weight: 400;
    white-space: nowrap;
  }
  /* Front */
  .card--front {
    background: linear-gradient(135deg, var(--orange-light) 0%, var(--bridge-orange) 50%, var(--orange-dark) 100%);
    display: flex;
    align-items: center;
    justify-content: center;
  }
  .card--front .wordmark { color: var(--paper); font-size: 30px; }
  /* Back */
  .card--back {
    background: linear-gradient(160deg, var(--paper) 55%, var(--paper-shade) 100%);
    font-family: "Questrial", sans-serif;
  }
  .card--back .wordmark {
    position: absolute;
    left: 72px;
    top: 26px;
    color: var(--ink);
    font-size: 26px;
  }
  .contact {
    position: absolute;
    left: 40px;
    top: 94px;
    font-size: 11.5px;
    color: var(--ink-soft);
    line-height: 1.45;
  }
  .contact__address { margin-bottom: 12px; }
  .contact__list { list-style: none; }
  .contact__list li { display: flex; align-items: center; gap: 8px; }
  .contact__icon { width: 10px; height: 10px; flex: none; }
  .holder {
    position: absolute;
    right: 34px;
    top: 158px;
    text-align: right;
  }
  .holder__name {
    font-family: "Arimo", sans-serif;
    font-weight: 700;
    font-size: 17px;
    color: var(--bridge-orange);
  }
  .holder__title { font-size: 12px; color: var(--muted); margin-top: 6px; }
  .accent-area {
    position: absolute;
    left: 0;
    bottom: 0;
    width: 330px;
    height: 64px;
    background: linear-gradient(180deg, rgba(232,100,26,0) 0%, rgba(232,100,26,.22) 100%);
  }
</style>
</head>
<body>
  <section class="card card--front" aria-label="Card front">
    <span class="wordmark">Kestrane Energy</span>
  </section>

  <section class="card card--back" aria-label="Card back">
    <span class="wordmark">Kestrane Energy</span>

    <div class="contact">
      <p class="contact__address">PO Box 40318<br>Oakland, CA 94612</p>
      <ul class="contact__list">
        <li>
          <svg class="contact__icon" viewBox="0 0 10 10"><circle cx="5" cy="5" r="5" fill="var(--bridge-orange)"/><path d="M3 2.5h1.3l.5 1.6-.8.6a4 4 0 0 0 1.6 1.6l.6-.8 1.6.5V7.5A5 5 0 0 1 3 2.5z" fill="#fff"/></svg>
          510.555.0147
        </li>
        <li>
          <svg class="contact__icon" viewBox="0 0 10 10"><circle cx="5" cy="5" r="5" fill="var(--bridge-orange)"/><rect x="3.4" y="2.2" width="3.2" height="5.6" rx=".6" fill="#fff"/></svg>
          510.555.0193
        </li>
        <li>
          <svg class="contact__icon" viewBox="0 0 10 10"><circle cx="5" cy="5" r="5" fill="var(--bridge-orange)"/><rect x="2.5" y="3.3" width="5" height="3.4" fill="#fff"/><path d="M2.5 3.3 5 5.3l2.5-2" fill="none" stroke="var(--bridge-orange)" stroke-width=".6"/></svg>
          whitfield@kestrane-energy.net
        </li>
        <li>
          <svg class="contact__icon" viewBox="0 0 10 10"><circle cx="5" cy="5" r="5" fill="var(--bridge-orange)"/><circle cx="5" cy="5" r="2.6" fill="none" stroke="#fff" stroke-width=".7"/><path d="M2.4 5h5.2M5 2.4v5.2" stroke="#fff" stroke-width=".6"/></svg>
          www.kestrane-energy.net
        </li>
      </ul>
    </div>

    <div class="holder">
      <p class="holder__name">Daniel Ross Whitfield</p>
      <p class="holder__title">CEO</p>
    </div>

    <div class="accent-area" role="img" aria-label="Decorative orange sweep along the lower left edge"></div>
  </section>
</body>
</html>
```